Business Card Design & logo

Residential building renovation and maintenance work.
All carpentry and joinery needs.
Laying solid timber and floating floors.
Kitchen and bathroom makeovers and modifications.
Interior fitouts,
small job specialist. tiling, plastering, painting,

I would like a silver background. With the use of different shades of grey, rustic orange, black and white.
I do not want pictures of hammers, chisels etc. I am looking for a logo to be incorporated into the card.

Industry/Entity Type

Carpentry

Contact Information for Business Card

BTW Renovations and Maintenance
Lionel Pasquet
0471526083
info@btwrefits.com.au
btwrefits.com.au

```html
<!DOCTYPE html>
<html lang="en">
<head>
<meta charset="utf-8">
<title>BTW Renovations and Maintenance – Business Cards</title>
<link href="https://fonts.googleapis.com/css2?family=Merriweather:wght@400;900&display=swap" rel="stylesheet">
<style>
  :root {
    --page: #ffffff;
    --band: #262626;
    --accent: #f2b705;
    --silver-light: #eeeeee;
    --silver-mid: #d6d6d6;
    --silver-dark: #bdbdbd;
    --ink: #2b2b2b;
    --ink-soft: #3a3a3a;
    --mark-light: #d9d9d9;
  }
  * { margin: 0; padding: 0; box-sizing: border-box; }
  html, body {
    width: 1200px; height: 798px; overflow: hidden;
    background: var(--page);
    font-family: "Merriweather", Georgia, serif;
  }
  .canvas { position: relative; width: 1200px; height: 798px; }

  .card {
    position: absolute;
    width: 520px; height: 312px;
    border-radius: 4px;
    overflow: hidden;
    background: linear-gradient(160deg, var(--silver-light) 0%, var(--silver-mid) 55%, var(--silver-dark) 100%);
    box-shadow: 0 6px 0 var(--band), 0 12px 24px rgba(0,0,0,.18);
  }
  .card--front { left: 50px; top: 110px; }
  .card--back  { left: 630px; top: 250px; }

  .card__band { position: absolute; inset: 0; width: 520px; height: 312px; }

  .brand {
    position: absolute;
    font-weight: 900;
    white-space: nowrap;
    letter-spacing: -0.5px;
  }
  .brand__mark {
    display: inline-block;
    width: 14px; height: 14px;
    background: var(--accent);
    margin-right: 8px;
    vertical-align: 1px;
  }
  .card--front .brand { left: 28px; top: 52px; font-size: 20px; color: var(--mark-light); }
  .card--back  .brand { left: 28px; top: 112px; font-size: 20px; color: var(--ink); }

  .side-block {
    position: absolute;
    left: 38px; top: 150px;
    width: 44px; height: 44px;
    background: var(--ink-soft);
  }
  .card--back .side-block { top: 178px; }

  .divider {
    position: absolute;
    left: 100px; top: 138px;
    width: 2px; height: 150px;
    background: var(--ink-soft);
  }
  .card--back .divider { top: 165px; height: 130px; }

  .contact { position: absolute; left: 116px; top: 110px; color: var(--ink); }
  .contact__name { font-size: 27px; font-weight: 900; margin-bottom: 10px; }
  .contact__line { font-size: 22px; font-weight: 400; line-height: 1.22; }

  .services {
    position: absolute; left: 116px; top: 170px;
    list-style: none; color: var(--ink);
    font-size: 15px; line-height: 1.45;
  }

  .lockup {
    position: absolute; left: 50px; top: 690px;
    font-size: 34px; font-weight: 900;
    color: var(--ink);
    white-space: nowrap;
    letter-spacing: -0.5px;
  }
  .lockup .brand__mark { width: 22px; height: 22px; margin-right: 12px; vertical-align: 0; }
</style>
</head>
<body>
<main class="canvas">

  <section class="card card--front" aria-label="Business card front">
    <svg class="card__band" viewBox="0 0 520 312" aria-hidden="true">
      <polygon points="0,0 520,0 520,78 0,104" fill="var(--band)"/>
      <polygon points="0,104 520,78 520,84 0,110" fill="var(--accent)"/>
    </svg>
    <div class="brand"><span class="brand__mark"></span>BTW Renovations and Maintenance</div>
    <div class="side-block" aria-hidden="true"></div>
    <div class="divider"></div>
    <div class="contact">
      <p class="contact__name">Lionel Pasquet</p>
      <p class="contact__line">0471526083</p>
      <p class="contact__line">info@btwrefits.com.au</p>
      <p class="contact__line">btwrefits.com.au</p>
    </div>
  </section>

  <section class="card card--back" aria-label="Business card back">
    <svg class="card__band" viewBox="0 0 520 312" aria-hidden="true">
      <polygon points="0,0 520,0 520,58 0,90" fill="var(--band)"/>
      <polygon points="0,90 520,58 520,64 0,96" fill="var(--accent)"/>
    </svg>
    <div class="brand"><span class="brand__mark"></span>BTW Renovations and Maintenance</div>
    <div class="side-block" aria-hidden="true"></div>
    <div class="divider"></div>
    <ul class="services">
      <li>Residential renovation &amp; maintenance</li>
      <li>All carpentry and joinery needs</li>
      <li>Laying solid timber and floating floors</li>
      <li>Kitchen &amp; bathroom modifications</li>
      <li>Interior fitouts</li>
      <li>Tiling, plastering &amp; painting</li>
    </ul>
  </section>

  <div class="lockup"><span class="brand__mark"></span>BTW Renovations and Maintenance</div>

</main>
</body>
</html>
```